Cafe Business needs a business card design

I already have an ai logo I would like to use and color. I need someone to make a business card for me on adobe illustrator with it. Its for a cafe restaurant opening in Japan I would like to be able to change out the names, contact info, ect on my own from adobe illustrator.

Industry/Entity Type

Business

Contact Information for Business Card

Double sided with logo on one side and info on the other. Name, Tel, fax, email and west

```html
<!DOCTYPE html>
<html lang="en">
<head>
<meta charset="utf-8">
<title>Hazel Kettle Cafe – Business Card</title>
<link rel="stylesheet" href="https://fonts.googleapis.com/css2?family=Source+Sans+3:ital,wght@0,400;0,600;1,400&display=swap">
<style>
  :root {
    --paper: #ffffff;
    --card: #ecdcc3;
    --brown: #3d2a1e;
    --ink: #2b211b;
  }
  * { margin: 0; padding: 0; box-sizing: border-box; }
  html, body {
    width: 1200px;
    height: 369px;
    overflow: hidden;
    background: var(--paper);
    font-family: "Source Sans 3", "Myriad Pro", Arial, sans-serif;
    color: var(--ink);
  }
  .canvas { position: relative; width: 1200px; height: 369px; }
  .card {
    position: absolute;
    top: 0;
    width: 574px;
    height: 369px;
    background: var(--card);
  }
  .card--front { left: 0; }
  .card--back { left: 626px; }

  .brand { position: absolute; text-align: center; color: var(--brown); }
  .brand__mark { display: block; background: var(--brown); margin: 0 auto; }
  .brand__name {
    display: block;
    font-weight: 600;
    text-transform: uppercase;
    letter-spacing: 0.04em;
    line-height: 1.05;
  }

  .brand--front { left: 130px; top: 38px; width: 314px; }
  .brand--front .brand__mark { width: 212px; height: 212px; }
  .brand--front .brand__name { font-size: 30px; margin-top: 10px; }
  .brand--front .brand__sub { font-size: 22px; letter-spacing: 0.3em; margin-top: 2px; }

  .brand--back { left: 386px; top: 186px; width: 140px; }
  .brand--back .brand__mark { width: 94px; height: 80px; }
  .brand--back .brand__name { font-size: 13px; margin-top: 6px; }
  .brand--back .brand__sub { font-size: 10px; letter-spacing: 0.3em; margin-top: 1px; }

  .holder { position: absolute; left: 49px; top: 108px; white-space: nowrap; }
  .holder__name { font-size: 27px; font-weight: 400; }
  .holder__role { font-size: 11px; font-style: italic; margin-left: 4px; }

  .contact {
    position: absolute;
    left: 49px;
    top: 264px;
    display: grid;
    grid-template-columns: 99px auto;
    row-gap: 4px;
    font-size: 18px;
    line-height: 22px;
  }
</style>
</head>
<body>
<main class="canvas">
  <section class="card card--front" aria-label="Card front">
    <div class="brand brand--front">
      <span class="brand__mark" aria-hidden="true"></span>
      <span class="brand__name">Hazel Kettle</span>
      <span class="brand__name brand__sub">Cafe</span>
    </div>
  </section>

  <section class="card card--back" aria-label="Card back">
    <p class="holder">
      <span class="holder__name">Owen Hartley</span><span class="holder__role">Manager</span>
    </p>
    <dl class="contact">
      <dt>Tel</dt><dd>0198765432</dd>
      <dt>Fax</dt><dd>0198765432</dd>
      <dt>Email</dt><dd>hello@hazelkettle.jp</dd>
    </dl>
    <div class="brand brand--back">
      <span class="brand__mark" aria-hidden="true"></span>
      <span class="brand__name">Hazel Kettle</span>
      <span class="brand__name brand__sub">Cafe</span>
    </div>
  </section>
</main>
</body>
</html>
```